Wordpress Corporate Website for New Business

We need a corporate website created which will act as a professional shop window for our new business. We do not need special features like merchant facilities or chatbots. The attachment shows suggested key sections as well as some possible wording. Various versions of the company logo have been attached as well to give different options to play with. We are looking for an option which is easy for us to take over and manage moving forward should we need to make minor updates.

Target Market(s)

Corporate entities

Industry/Entity Type

Private share auctions

Coding

Coded - Design and coding required

```html
<!DOCTYPE html>
<html lang="en">
<head>
<meta charset="utf-8">
<title>ShareVale – Private Share Auctions</title>
<link href="https://fonts.googleapis.com/css2?family=Poppins:wght@400;500;600;700;800&display=swap" rel="stylesheet">
<style>
:root{
  --purple:#8a0a98;
  --purple-dark:#6e0679;
  --ink:#1c1c1c;
  --text:#3a3a3a;
  --muted:#777;
  --light:#f4f4f5;
  --mint:#eef8f8;
  --white:#fff;
  --black:#000;
  --icon-bg:#e8e8ea;
}
*{margin:0;padding:0;box-sizing:border-box}
html,body{width:1200px;height:4054px;overflow:hidden}
body{font-family:'Poppins',sans-serif;color:var(--text);background:var(--white);position:relative}
.abs{position:absolute}
a{color:inherit;text-decoration:none}
.btn{position:absolute;background:var(--purple);color:var(--white);font-size:16px;display:flex;align-items:center;justify-content:center;border-radius:2px}

/* top bar */
.topbar{left:0;top:0;width:1200px;height:55px;background:var(--light);border-bottom:1px solid #e4e4e4}
.topbar .contacts{position:absolute;left:83px;top:19px;display:flex;gap:28px;white-space:nowrap}
.topbar .contact{font-size:12px;line-height:14px;color:#555;display:flex;align-items:center;gap:8px}
.topbar .contact i{flex:none;width:18px;height:12px;background:#2b3aa0;border-radius:2px;display:inline-block}
.topbar .social{position:absolute;right:82px;top:18px;display:flex;gap:16px}
.dot{width:18px;height:18px;border-radius:50%;border:2px solid #555;display:inline-block}

/* header */
.header{left:0;top:55px;width:1200px;height:85px;background:var(--white);border-bottom:1px solid #e4e4e4}
.brand{position:absolute;left:83px;top:26px;display:flex;align-items:center;gap:8px;font-weight:600;font-size:28px;color:var(--purple)}
.brand .mark{width:30px;height:30px;border-radius:50%;background:var(--purple)}
.nav{position:absolute;right:214px;top:33px;display:flex;gap:14px;font-size:12px;color:#444}
.nav .active{color:var(--purple);border-bottom:1px solid var(--purple)}
.book{right:93px;top:27px;width:109px;height:31px;border-radius:16px;font-size:13px}

/* hero */
.hero{left:0;top:140px;width:1200px;height:528px;background:linear-gradient(100deg,#3a3b3f 0%,#5a5c62 40%,#8d8f95 70%,#b9b5b2 100%)}
.hero h1{position:absolute;left:83px;top:104px;width:520px;color:var(--white);font-size:37px;line-height:56px;font-weight:800}
.hero p{position:absolute;left:83px;top:236px;width:500px;color:#eee;font-size:14.5px;line-height:29px}
.hero .btn{left:83px;top:347px;width:158px;height:44px}
.arrow{position:absolute;top:240px;width:50px;height:50px;border-radius:50%;display:flex;align-items:center;justify-content:center}

.info-card{top:600px;width:410px;height:334px;background:var(--white);border-radius:12px;box-shadow:0 6px 20px rgba(0,0,0,.08);border-bottom:14px solid var(--purple)}
.info-card .ico{position:absolute;left:40px;top:35px;width:92px;height:86px;background:var(--icon-bg);border-radius:4px;display:flex;align-items:center;justify-content:center}
.info-card h3{position:absolute;left:40px;top:148px;font-size:19px;font-weight:600;color:var(--ink)}
.info-card p{position:absolute;left:40px;top:190px;width:305px;font-size:14.5px;line-height:29px;color:#333}

/* about */
.about{left:0;top:1008px;width:1200px;height:546px;background:linear-gradient(90deg,#f6f6f7,#fafafa 60%,#f1f2f3)}
.about h2{position:absolute;left:85px;top:112px;font-size:30px;font-weight:600;color:#444}
.about p{position:absolute;left:83px;top:175px;width:555px;font-size:15px;line-height:35px;color:#333}
.about .btn{left:83px;top:378px;width:158px;height:43px}
.about .frame{position:absolute;left:710px;top:220px;width:406px;height:210px;background:var(--purple);border-radius:10px}
.about .photo{position:absolute;left:655px;top:111px;width:453px;height:303px;border-radius:8px;background:linear-gradient(120deg,#6f8896 0%,#a7b8c1 45%,#d8dfe2 70%,#9a8a75 100%)}

/* why */
.why{left:0;top:1554px;width:1200px;height:939px;background:var(--mint)}
.why .eyebrow{position:absolute;left:83px;top:178px;font-size:13px;font-weight:600;color:#444}
.why h2{position:absolute;left:83px;top:200px;width:300px;font-size:40px;line-height:62px;font-weight:600;color:var(--ink)}
.why p{position:absolute;left:83px;top:323px;width:290px;font-size:14.5px;line-height:34px;color:#333}
.why .btn{left:83px;top:484px;width:145px;height:41px}
.feat{position:absolute;width:328px;height:190px;background:var(--white);border-radius:14px;box-shadow:2px 3px 8px rgba(0,0,0,.08)}
.feat svg{position:absolute;left:24px;top:34px}
.feat h4{position:absolute;left:78px;top:36px;font-size:16px;font-weight:500;color:var(--ink)}
.feat p{position:absolute;left:78px;top:64px;width:232px;font-size:13.5px;line-height:26.5px;color:#333}
.feat a{position:absolute;left:78px;top:147px;font-size:13px;color:var(--purple);text-decoration:underline}

/* team */
.team{left:0;top:2493px;width:1200px;height:893px;background:linear-gradient(90deg,#f3f3f4,#ececee 50%,#f2f2f3)}
.team .eyebrow{position:absolute;width:1200px;text-align:center;top:80px;font-size:28px;font-weight:600;color:#444}
.team h2{position:absolute;width:1200px;text-align:center;top:124px;font-size:40px;font-weight:600;color:var(--ink)}
.member{position:absolute;top:224px;width:304px;height:504px;background:var(--white);border-radius:0 0 30px 30px;overflow:hidden;box-shadow:0 4px 10px rgba(0,0,0,.06)}
.member .portrait{height:409px}
.member .name{text-align:center;margin-top:14px;font-size:23px;font-weight:500;color:var(--purple)}
.member .role{text-align:center;font-size:16px;color:#222;margin-top:-4px}
.member .socials{position:absolute;left:24px;top:158px;display:flex;flex-direction:column;gap:17px}
.member .socials span{width:37px;height:37px;border-radius:50%;background:#eee;display:flex;align-items:center;justify-content:center}
.member .socials span i{width:15px;height:15px;border-radius:50%;border:2px solid var(--purple)}

/* footer */
.footer{left:0;top:3386px;width:1200px;height:668px;background:var(--black);color:var(--white)}
.newsletter{left:83px;top:3287px;width:1034px;height:230px;background:var(--white);border-radius:4px}
.newsletter h3{position:absolute;left:127px;top:47px;font-size:35px;font-weight:500;color:var(--ink)}
.newsletter p{position:absolute;left:128px;top:107px;width:360px;font-size:11.5px;line-height:29px;color:#333}
.newsletter .field{position:absolute;left:553px;top:93px;width:342px;height:43px;background:#ddd;font-size:13px;color:#aaa;padding:13px 18px}
.newsletter .send{left:892px;top:93px;width:90px;height:43px;font-weight:600;font-size:15px}
.newsletter svg{position:absolute;left:50px;top:46px}

.fbrand{position:absolute;left:139px;top:180px;display:flex;flex-direction:column;gap:10px}
.fbrand .mark{width:84px;height:84px;border-radius:50%;background:var(--purple);margin-left:66px}
.fbrand .word{font-size:46px;font-weight:600;color:var(--purple);line-height:1}
.footer .about-txt{position:absolute;left:139px;top:330px;width:325px;font-size:13px;line-height:19.5px;color:#ddd}
.footer .pill{position:absolute;left:139px;top:458px;width:117px;height:37px;background:var(--white);color:#111;border-radius:19px;font-size:14px;display:flex;align-items:center;justify-content:center}
.footer .soc{position:absolute;left:139px;top:506px;display:flex;gap:8px}
.footer .soc .dot{width:17px;height:17px;border-color:#fff}
.fnav{position:absolute;right:83px;top:204px;display:flex;gap:24px;font-size:15px}
.fcol{position:absolute;top:286px}
.fcol h5{font-size:13px;font-weight:400;color:#aaa;padding-bottom:8px;border-bottom:1px solid var(--purple);width:138px}
.fcol ul{list-style:none;margin-top:23px}
.fcol li{font-size:13px;height:35.6px;color:#eee}
.fline{position:absolute;left:139px;top:607px;width:940px;height:1px;background:#666}
.fbottom{position:absolute;top:632px;font-size:13px;color:#eee}
</style>
</head>
<body>

<div class="abs topbar">
  <div class="contacts">
    <div class="contact"><i></i>hello@sharevale.example</div>
    <div class="contact"><i></i>+65 9000 4821</div>
  </div>
  <div class="social"><span class="dot"></span><span class="dot"></span><span class="dot"></span></div>
</div>

<header class="abs header">
  <div class="brand"><span class="mark"></span>ShareVale</div>
  <nav class="nav">
    <a class="active">Home</a><a>About Us</a><a>Our Team</a><a>Key Features</a><a>Contact Us</a>
  </nav>
  <a class="btn book">Book Now</a>
</header>

<section class="abs hero" role="img" aria-label="Photo of a business team collaborating around a desk">
  <h1>Retain Control, Unlock Liquidity</h1>
  <p>Lorem Ipsum is simply dummy text of the printing and typesetting industry. Lorem Ipsum has been the industry's standard dummy text ever since the 1500s.</p>
  <a class="btn">Read More</a>
  <div class="arrow" style="left:32px"><svg width="16" height="24"><path d="M12 3 L4 12 L12 21" stroke="#fff" stroke-width="3" fill="none"/></svg></div>
  <div class="arrow" style="right:32px;background:rgba(0,0,0,.55)"><svg width="16" height="24"><path d="M4 3 L12 12 L4 21" stroke="#fff" stroke-width="3" fill="none"/></svg></div>
</section>

<div class="abs info-card" style="left:178px">
  <div class="ico"><svg width="44" height="56" viewBox="0 0 44 56"><rect x="2" y="2" width="40" height="52" fill="#8a0a98"/><g fill="#fff"><rect x="10" y="10" width="7" height="7"/><rect x="27" y="10" width="7" height="7"/><rect x="10" y="24" width="7" height="7"/><rect x="27" y="24" width="7" height="7"/><rect x="18" y="40" width="8" height="14"/></g></svg></div>
  <h3>Company</h3>
  <p>This might explain what we do to help the company roll this out and the process, including engagement...</p>
</div>
<div class="abs info-card" style="left:613px">
  <div class="ico"><svg width="58" height="58" viewBox="0 0 58 58"><circle cx="29" cy="12" r="7" fill="none" stroke="#8a0a98" stroke-width="5"/><path d="M26 18 L10 52 M32 18 L48 52 M8 38 Q29 50 50 36" stroke="#8a0a98" stroke-width="6" fill="none" stroke-linecap="round"/></svg></div>
  <h3>Shareholder</h3>
  <p>Example of the login process, what features the platform has and what happens post a transaction...</p>
</div>

<section class="abs about">
  <h2>About Us</h2>
  <p>At ShareVale, we empower private companies to take control of their share transactions without the hassle of third-party involvement. Our innovative share exchange platform is designed to connect pre-approved buyers and sellers directly, fostering a secure and efficient environment for trading ownership in private enterprises.</p>
  <a class="btn">Read More</a>
  <div class="frame"></div>
  <div class="photo" role="img" aria-label="Photo of two business people shaking hands across a table"></div>
</section>

<section class="abs why">
  <div class="eyebrow">Why Choose ShareVale?</div>
  <h2>Explore What We Offer</h2>
  <p>Lorem Ipsum is simply dummy text of the printing and typesetting industry. Lorem Ipsum has been the industry's standard dummy text.</p>
  <a class="btn">View More</a>

  <div class="feat" style="left:436px;top:115px">
    <svg width="36" height="46"><rect x="2" y="2" width="32" height="42" fill="#8a0a98"/><g fill="#fff"><rect x="9" y="8" width="6" height="6"/><rect x="21" y="8" width="6" height="6"/><rect x="9" y="20" width="6" height="6"/><rect x="21" y="20" width="6" height="6"/><rect x="15" y="33" width="6" height="11"/></g></svg>
    <h4>Retain Control</h4><p>Companies can maintain control over who participates in their auctions...</p><a>Read More</a>
  </div>
  <div class="feat" style="left:786px;top:115px">
    <svg width="40" height="46"><path d="M12 20 V12 a10 10 0 0 1 20 0" stroke="#8a0a98" stroke-width="5" fill="none"/><rect x="2" y="20" width="32" height="24" rx="3" fill="#8a0a98"/><circle cx="18" cy="32" r="4" fill="#fff"/></svg>
    <h4>Unlock Liquidity</h4><p>ShareVale provides a structured marketplace which facilitates efficient...</p><a>Read More</a>
  </div>
  <div class="feat" style="left:436px;top:359px">
    <svg width="44" height="40"><rect x="2" y="8" width="40" height="26" rx="4" fill="none" stroke="#8a0a98" stroke-width="4"/><rect x="2" y="15" width="40" height="5" fill="#8a0a98"/></svg>
    <h4>Direct Transactions</h4><p>Say goodbye to intermediaries. Our platform enables shareholders...</p><a>Read More</a>
  </div>
  <div class="feat" style="left:789px;top:359px">
    <svg width="46" height="40"><circle cx="14" cy="10" r="8" fill="#8a0a98"/><path d="M0 38 a14 14 0 0 1 28 0 Z" fill="#8a0a98"/><rect x="26" y="22" width="18" height="16" rx="2" fill="#8a0a98"/><path d="M30 22 v-5 a5 5 0 0 1 10 0 v5" stroke="#8a0a98" stroke-width="3" fill="none"/></svg>
    <h4>Secure and Confidential</h4><p>We understand the importance of privacy. Our security measures safeguard your sensitive...</p><a>Read More</a>
  </div>
  <div class="feat" style="left:83px;top:604px">
    <svg width="36" height="36"><circle cx="18" cy="18" r="16" fill="#8a0a98"/><path d="M8 10 q8 4 6 12 q6 2 4 10 M24 6 q-2 8 8 10" stroke="#fff" stroke-width="3" fill="none"/></svg>
    <h4>Global Reach</h4><p>Our platform allows companies and investors from around the world to connect...</p><a>Read More</a>
  </div>
  <div class="feat" style="left:433px;top:604px">
    <svg width="40" height="34"><path d="M20 2 V30 M10 32 H30 M4 8 H36" stroke="#8a0a98" stroke-width="3"/><path d="M0 20 L6 8 L12 20 Z M28 20 L34 8 L40 20 Z" fill="none" stroke="#8a0a98" stroke-width="2.5"/></svg>
    <h4>Scalability</h4><p>The ShareVale platform can scale to accommodate the needs of companies...</p><a>Read More</a>
  </div>
  <div class="feat" style="left:787px;top:604px">
    <svg width="40" height="40"><path d="M20 2 L32 16 H24 V28 H16 V16 H8 Z" fill="#8a0a98"/><path d="M2 26 V36 H38 V26" stroke="#8a0a98" stroke-width="4" fill="none"/></svg>
    <h4>Price Discovery</h4><p>Private share auctions help establish fair market values for shares, as the...</p><a>Read More</a>
  </div>
</section>

<section class="abs team">
  <div class="eyebrow">Our Team</div>
  <h2>Meet The Expert</h2>
  <div class="member" style="left:83px">
    <div class="portrait" role="img" aria-label="Portrait photo of a team member in a dark suit" style="background:linear-gradient(160deg,#2d2f33,#1f2022 60%,#3a3c40)"></div>
    <div class="socials"><span><i></i></span><span><i></i></span><span><i></i></span></div>
    <div class="name">Maya Linden</div><div class="role">Financial Advisor</div>
  </div>
  <div class="member" style="left:447px">
    <div class="portrait" role="img" aria-label="Portrait photo of a team member in black attire" style="background:linear-gradient(160deg,#3a3a3c,#1d1d1f 70%)"></div>
    <div class="name">Maya Linden</div><div class="role">Financial Advisor</div>
  </div>
  <div class="member" style="left:811px">
    <div class="portrait" role="img" aria-label="Portrait photo of a team member in a grey blazer" style="background:linear-gradient(160deg,#8a8c92,#6d6f75 60%,#55575c)"></div>
    <div class="name">Maya Linden</div><div class="role">Financial Advisor</div>
  </div>
</section>

<footer class="abs footer">
  <div class="fbrand"><span class="mark"></span><span class="word">ShareVale</span></div>
  <p class="about-txt">Lorem Ipsum is simply dummy text of the printing and typesetting industry. Lorem Ipsum has been the industry's standard dummy text ever since the 1500s</p>
  <a class="pill">About us</a>
  <div class="soc"><span class="dot"></span><span class="dot"></span><span class="dot"></span></div>
  <nav class="fnav"><a>Home</a><a>About us</a><a>Our Team</a><a>Key Features</a><a>Why Choose us</a><a>Contact Us</a></nav>
  <div class="fcol" style="left:556px"><h5>Resources</h5><ul><li>Home</li><li>About</li><li>Our Team</li><li>Key Features</li><li>Why Choose Us</li><li>Contact Us</li></ul></div>
  <div class="fcol" style="left:850px"><h5>Other Links</h5><ul><li>Retain Control</li><li>Unlock Liquidity</li><li>Direct Transactions</li><li>Global Reach</li><li>Scalability</li><li>Price Discovery</li></ul></div>
  <div class="fline"></div>
  <div class="fbottom" style="left:139px">Copyright by ShareVale</div>
  <div class="fbottom" style="left:773px">Privacy Policy</div>
  <div class="fbottom" style="left:880px">Legal Agreement</div>
</footer>

<div class="abs newsletter">
  <svg width="56" height="50"><rect x="12" y="2" width="40" height="28" rx="3" fill="#8a0a98"/><rect x="2" y="18" width="40" height="28" rx="3" fill="#8a0a98" stroke="#fff" stroke-width="3"/><path d="M4 20 L22 34 L40 20" stroke="#fff" stroke-width="3" fill="none"/></svg>
  <h3>Newsletter</h3>
  <p>Lorem Ipsum is simply dummy text of the printing and typesetting industry. Lorem Ipsum has been the industry's standard dummy text ever since the 1500s.</p>
  <div class="field">Your E-Mail</div>
  <a class="btn send">SEND</a>
</div>

</body>
</html>
```